Graphic picture for front page of website

We need a picture to place on the front page of our pressloft Website. The company name is Nova Grid , and we sell Tessary Sheets services. The website is www.novagridsheets.example . I am looking for something to go in the picture in the middle of the site, to replace the current default template. Currently we use the color green, as it is default, but happy for you to be creative to see what works (colorful is good). I have included just some random screenshots of projects I have done for clients, for some possible inspiration. Have a look at our services to see what kinds of work we do.
We currently have no logo, the lumora thing is just a default of the pressloft theme.
Updates
Hi guys, I have uploaded a picture to show you the dimensions (the ratio, please make the image large so it is very high quality, i can scale it to the exact size needed). All of the writing/key info should be in the red lines, people with smaller monitors will just see that, people with wide monitors will see all of it.
Thanks
No stock photos of people thanks.
Target Market(s)
Small to large business, looking for Tessary Sheets services.
Industry/Entity Type
It Company
Look and feel
Each slider illustrates characteristics of the customer's brand and the style your logo design should communicate.

```html
<!DOCTYPE html>
<html lang="en">
<head>
<meta charset="utf-8">
<title>Nova Grid – Run Macro</title>
<link rel="stylesheet" href="https://fonts.googleapis.com/css2?family=Nunito+Sans:wght@300;400&family=Arimo:wght@400;700&display=swap">
<style>
  :root {
    --panel-navy: #1b5a7e;
    --stage-blue: #3d88b6;
    --sheet-white: #ffffff;
    --cell-line: #e3e3e3;
    --ink: #111111;
    --cell-green: #92d050;
    --header-green: #00a650;
    --pale-green: #c6e6a4;
    --plot-grey: #d9d9d9;
    --zone-yellow: #f2f200;
    --zone-amber: #e0a800;
    --zone-rust: #cf7a10;
    --limit-red: #ff2a1a;
    --button-grey: #efefef;
  }
  * { box-sizing: border-box; margin: 0; padding: 0; }
  html, body { width: 1200px; height: 460px; overflow: hidden; background: var(--stage-blue); }
  .hero { position: relative; width: 1200px; height: 460px; background: var(--stage-blue); }
  .hero__intro {
    position: absolute; left: 0; top: 0; width: 412px; height: 460px;
    background: var(--panel-navy); color: #fff; text-align: center;
    font-family: "Nunito Sans", sans-serif;
  }
  .hero__brand { position: absolute; top: 53px; width: 100%; font-size: 13px; font-weight: 400; }
  .hero__title {
    position: absolute; top: 155px; width: 100%;
    font-size: 42px; font-weight: 300; line-height: 55px; letter-spacing: 1px;
  }
  .hero__lede {
    position: absolute; top: 318px; left: 110px; width: 192px;
    font-size: 14px; font-weight: 300; line-height: 18px;
  }
  .hero__sheet { position: absolute; left: 0; top: 0; }
  .sheet-text { font-family: Arimo, sans-serif; }
</style>
</head>
<body>
<main class="hero">
  <section class="hero__intro">
    <p class="hero__brand">nova grid</p>
    <h1 class="hero__title">RUN<br>MACRO</h1>
    <p class="hero__lede">Lorem Ipsum is simply dummy text of the printing and typesetting industry.</p>
  </section>

  <svg class="hero__sheet" width="1200" height="460" viewBox="0 0 1200 460" aria-label="Spreadsheet with beam span chart">
    <defs>
      <pattern id="cells" x="436" y="30" width="64" height="18" patternUnits="userSpaceOnUse">
        <path d="M64 0V18M0 18H64" stroke="var(--cell-line)" stroke-width="1" fill="none"/>
      </pattern>
      <pattern id="minor" x="565" y="108" width="9.1" height="9.2" patternUnits="userSpaceOnUse">
        <path d="M9.1 0V9.2M0 9.2H9.1" stroke="#555" stroke-width="0.5" fill="none"/>
      </pattern>
      <pattern id="major" x="565" y="108" width="45.5" height="46" patternUnits="userSpaceOnUse">
        <path d="M0 0V46M0 0H45.5" stroke="#222" stroke-width="1.1" fill="none"/>
      </pattern>
    </defs>

    <!-- worksheet -->
    <rect x="436" y="30" width="750" height="400" fill="var(--sheet-white)"/>
    <rect x="436" y="30" width="750" height="400" fill="url(#cells)"/>
    <rect x="482" y="30" width="704" height="363" fill="var(--sheet-white)" stroke="var(--ink)" stroke-width="2"/>

    <!-- input cells -->
    <rect x="458" y="165" width="25" height="88" fill="var(--cell-green)" stroke="#555"/>
    <text class="sheet-text" x="475" y="209" font-size="15" text-anchor="middle" transform="rotate(-90 475 209)" fill="var(--ink)">4000</text>
    <rect x="735" y="393" width="95" height="25" fill="var(--cell-green)" stroke="#555"/>
    <text class="sheet-text" x="782" y="412" font-size="16" text-anchor="middle" fill="var(--ink)">7000</text>

    <!-- macro button -->
    <rect x="1059" y="43" width="85" height="28" fill="var(--button-grey)" stroke="#999"/>
    <path d="M1144 43V71H1059" stroke="#666" fill="none"/>
    <text class="sheet-text" x="1101" y="62" font-size="12" text-anchor="middle" fill="var(--ink)">Run Macro</text>

    <!-- result -->
    <rect x="1077" y="153" width="83" height="37" fill="var(--header-green)" stroke="#333"/>
    <text class="sheet-text" x="1118" y="168" font-size="10" text-anchor="middle" fill="var(--ink)">Recommended</text>
    <text class="sheet-text" x="1118" y="182" font-size="10" text-anchor="middle" fill="var(--ink)">Beam</text>
    <rect x="1077" y="190" width="83" height="38" fill="var(--pale-green)" stroke="#333"/>
    <text class="sheet-text" x="1118" y="218" font-size="22" text-anchor="middle" fill="var(--ink)">235</text>
    <text class="sheet-text" x="1118" y="253" font-size="22" text-anchor="middle" fill="var(--ink)">BV51</text>

    <!-- chart title -->
    <circle cx="723" cy="90" r="8" fill="none" stroke="var(--ink)"/>
    <text class="sheet-text" x="723" y="94" font-size="10" text-anchor="middle" fill="var(--ink)">A</text>
    <text class="sheet-text" x="735" y="94" font-size="11" fill="var(--ink)">- No Overhang</text>

    <!-- plot -->
    <rect x="565" y="108" width="455" height="230" fill="var(--plot-grey)"/>
    <polygon points="610.5,338 610.5,131 915,131 974.5,241 974.5,338" fill="var(--zone-rust)"/>
    <polygon points="610.5,338 610.5,131 815,131 837,190 880,240 920,287 920,338" fill="var(--zone-amber)"/>
    <polygon points="610.5,338 610.5,131 710.6,131 838,292 838,338" fill="var(--zone-yellow)"/>
    <rect x="565" y="108" width="455" height="230" fill="url(#minor)"/>
    <rect x="565" y="108" width="455" height="230" fill="url(#major)"/>
    <rect x="565" y="108" width="455" height="230" fill="none" stroke="#222" stroke-width="1.2"/>
    <g stroke="var(--limit-red)" stroke-width="2.2" fill="none">
      <polyline points="710.6,131 838,292 838,338"/>
      <polyline points="815,131 837,190 880,240 920,287 920,338"/>
      <polyline points="915,131 974.5,241 974.5,338"/>
    </g>

    <!-- axes -->
    <g class="sheet-text" font-size="9" font-weight="700" fill="var(--ink)" text-anchor="end">
      <text x="553" y="115">5000</text>
      <text x="553" y="161">4000</text>
      <text x="553" y="207">3000</text>
      <text x="553" y="253">2000</text>
      <text x="553" y="299">1000</text>
      <text x="553" y="345">0</text>
    </g>
    <g class="sheet-text" font-size="9" font-weight="700" fill="var(--ink)">
      <text transform="translate(607 345) rotate(90)">1000</text>
      <text transform="translate(652 345) rotate(90)">2000</text>
      <text transform="translate(698 345) rotate(90)">3000</text>
      <text transform="translate(743 345) rotate(90)">4000</text>
      <text transform="translate(789 345) rotate(90)">5000</text>
      <text transform="translate(834 345) rotate(90)">6000</text>
      <text transform="translate(880 345) rotate(90)">7000</text>
      <text transform="translate(925 345) rotate(90)">8000</text>
      <text transform="translate(971 345) rotate(90)">9000</text>
      <text transform="translate(1016 345) rotate(90)">10000</text>
    </g>
    <text class="sheet-text" x="792" y="385" font-size="10" font-weight="700" text-anchor="middle" fill="var(--ink)">Head Beam Span (mm)</text>
    <text class="sheet-text" x="508" y="223" font-size="10" font-weight="700" text-anchor="middle" transform="rotate(-90 508 223)" fill="var(--ink)">Sheet Span (mm)</text>
  </svg>
</main>
</body>
</html>
```